Premium Fitness Meal Plan Design for VoltaKor (Brand Like PlumQuarry!)

VoltaKor 6 Week Autumn Forge Meal Plan Design (Branded Handout)

πŸ“„ Overview:
We are looking for a professionally designed, branded meal plan handout for our fitness facility, VoltaKor. This meal plan will be used during our upcoming 6 Week Autumn Forge Quest, where members aim to lose body fat, build lean muscle, and improve their energy through nutrition and strength training.

The design should be highly polished, visually engaging, and reflect our brand quality β€” something on par with what you would see from larger national gym chains (e.g., Plum Quarry, K62, Delmar’s Drillyard). This is not just a text document β€” we want it to feel premium, motivating, and easy to follow, ideally something members are excited to reference and share.

🧾 Format & Layout:
Size: Standard 8.5x11 inch format (single or double-sided)

Final Output: Print-ready PDF + editable source files

Orientation: Portrait

Can be designed as either:

One visually organized front-and-back sheet

Or two clean, digestible pages presented as a mini-handout

🎨 Design Style:
Clean, energetic, and transformation-focused

Use brand colors and fonts that feel bold, fresh, and motivating

Include icons, dividers, or visual cues to separate sections (not just blocks of text)

Sections should feel approachable and empowering, not clinical or restrictive

Include room for the VoltaKor logo (provided) at the top and/or footer

πŸ“˜ Content to Include:
The following content should be visually structured and formatted in clear, engaging blocks. We’ll provide this content in a PDF format

1. Header Title:
"VoltaKor 6 Week Autumn Forge Nutrition Blueprint"

2. Introduction (Small Block):
Short blurb about the challenge goals (lose body fat, gain energy, preserve lean muscle mass)

3. Elimination List (Foods to Avoid):
A visually separated section with a list of foods and drinks that should be eliminated or greatly reduced for fat loss

4. Smart Swaps Table:
A side-by-side "Craving vs Swap" table that shows easy alternatives to popular bad habits (e.g., soda β†’ sparkling water)

5. Build-Your-Own Meal Plan Sections:
Organize these into clear categories:

Proteins

Carbs

Fats

Veggies

Extras / Smart Swaps
Use icons, color codes, or visual grids to organize these food lists

6. Tips Section (Optional Bonuses):
Hydration goal

Suggested number of meals

Protein shake recommendation

Meal timing tip

10-min walk after dinner tip

πŸ“¦ Files Provided:

All written content in organized text format

βœ… Deliverables:
Final design in print-ready PDF

Editable source file (AI, PSD, or InDesign preferred)

πŸ™Œ Inspiration:
Design should feel in line with the type of professional print materials used by high-end fitness studios. Clean lines, engaging fonts, and premium layout. We're not looking for clipart or gimmicky stock photos β€” we want the design to reflect the premium, results-driven experience our gym provides.

```html
<!DOCTYPE html>
<html lang="en">
<head>
<meta charset="utf-8">
<title>VoltaKor 6 Week Autumn Forge Nutrition Blueprint</title>
<link href="https://fonts.googleapis.com/css2?family=Archivo+Black&family=Montserrat:wght@400;500;600;700;800;900&display=swap" rel="stylesheet">
<style>
  :root{
    --yellow:#f9d00f;
    --orange:#f7941d;
    --blue:#3a4fb8;
    --green:#3fae49;
    --black:#0b0b0b;
    --ink:#ffffff;
    --line:#3a3a3a;
    --canvas:#e6e6e6;
  }
  *{box-sizing:border-box;margin:0;padding:0}
  html,body{width:847px;height:1200px;overflow:hidden;background:var(--canvas)}
  body{position:relative;font-family:"Montserrat",sans-serif;color:var(--ink)}
  .sheet{position:absolute;left:196px;width:690px;height:893px;background:var(--black);transform-origin:0 0;transform:scale(0.658);overflow:hidden}
  .sheet--blueprint{top:8px}
  .sheet--guide{top:605px}
  .abs{position:absolute}
  .display{font-family:"Archivo Black",sans-serif;text-transform:uppercase;line-height:.95}

  /* page 1 */
  .hero-photo{left:0;top:0;width:690px;height:250px;background:linear-gradient(180deg,#2a2a2a 0%,#161616 60%,var(--black) 100%)}
  .title-week{left:55px;top:30px;font-size:66px;color:var(--ink)}
  .title-season{left:55px;top:96px;font-size:64px;color:var(--yellow)}
  .title-forge{left:55px;top:154px;font-size:64px;color:var(--yellow)}
  .title-sub{left:300px;top:160px;font-size:25px;color:var(--ink);line-height:1}
  .brand{left:440px;top:42px;text-align:center}
  .brand-name{font-family:"Archivo Black",sans-serif;font-size:44px;color:var(--yellow);line-height:1}
  .brand-tag{font-size:7px;font-weight:800;color:var(--yellow);letter-spacing:2px;margin-top:4px}
  .goal-label{left:478px;top:172px;font-family:"Archivo Black",sans-serif;font-size:28px;color:var(--green);transform:rotate(-90deg);transform-origin:left top;width:100px}
  .goal-head{left:522px;top:126px;font-size:12px;font-weight:900;color:var(--orange);line-height:1.05}
  .goal-body{left:522px;top:180px;width:140px;font-size:12px;font-weight:500;line-height:1.2}

  .eliminate{left:55px;top:240px;width:268px;height:620px;border:1.5px solid var(--yellow);border-left:none;border-top:none;border-radius:0 0 18px 0}
  .eliminate::before{content:"";position:absolute;right:-1.5px;top:0;height:28px;border-right:1.5px solid var(--yellow)}
  .elim-title{position:absolute;left:0;top:14px;font-size:22px}
  .elim-title .orange{color:var(--orange)}
  .elim-note{position:absolute;left:0;top:78px;font-size:13px;font-weight:800}
  .elim-desc{position:absolute;left:0;top:97px;width:240px;font-size:10.5px;font-weight:600;color:var(--yellow);line-height:1.2}
  .elim-list{position:absolute;left:0;top:140px;list-style:none;width:250px}
  .elim-list li{display:flex;align-items:flex-start;height:47.5px}
  .elim-icon{flex:none;width:32px;height:32px;border-radius:50%;border:1.5px solid var(--yellow);margin-right:14px;display:flex;align-items:center;justify-content:center}
  .elim-icon span{width:16px;height:16px;border-radius:4px;background:linear-gradient(135deg,var(--orange),#d9453b)}
  .elim-item b{display:block;font-size:13px;font-weight:800;line-height:1.05}
  .elim-item small{display:block;font-size:9.5px;font-weight:600;color:var(--yellow);line-height:1.15}

  .swaps-title{left:340px;top:262px;width:315px;text-align:center;font-size:37px}
  .swaps-title .yellow{color:var(--yellow)}
  .swaps-desc{left:340px;top:346px;width:315px;text-align:center;font-size:11.5px;font-weight:500;line-height:1.2}
  .pill{position:absolute;display:flex;align-items:center;justify-content:center;font-weight:800;border-radius:3px}
  .pill--craving{left:342px;top:405px;width:106px;height:26px;background:var(--orange);color:var(--black);font-size:16px}
  .pill--instead{left:464px;top:405px;width:186px;height:26px;background:var(--blue);color:var(--ink);font-size:16px}
  .swap-table{left:342px;top:440px;width:315px;border-collapse:collapse}
  .swap-table td{height:40px;border-bottom:1px solid var(--line);vertical-align:middle}
  .swap-craving{width:84px;padding-left:10px;font-size:12px;font-weight:800;color:var(--orange);line-height:1.05}
  .swap-arrow{width:50px}
  .swap-arrow svg{display:block;margin-left:6px}
  .swap-text{font-size:9.5px;font-weight:500;line-height:1.2}

  /* page 2 */
  .guide-kicker{left:0;top:22px;width:690px;text-align:center;font-size:26px;letter-spacing:6px}
  .guide-title{left:0;top:52px;width:690px;text-align:center;font-size:44px;letter-spacing:7px;color:var(--yellow)}
  .guide-intro{left:0;top:101px;width:690px;text-align:center;font-size:12.5px;font-weight:800;line-height:1.25}
  .c-blue{color:#5b72f2}.c-orange{color:var(--orange)}.c-green{color:var(--green)}
  .food-col{top:172px;width:152px;height:355px;border:1.5px solid #5a5a5a;border-radius:10px;padding:30px 10px 0 12px}
  .col-pill{position:absolute;left:50%;top:-12px;transform:translateX(-50%);width:112px;height:25px;border-radius:12px;font-family:"Archivo Black",sans-serif;font-size:16px;display:flex;align-items:center;justify-content:center}
  .col-pill--proteins{background:var(--blue);color:var(--ink)}
  .col-pill--carbs{background:var(--yellow);color:var(--black)}
  .col-pill--fats{background:var(--orange);color:var(--black)}
  .col-pill--veggies{background:var(--green);color:var(--black)}
  .col-note{text-align:center;font-size:9.5px;font-weight:800;line-height:1.15;margin-bottom:12px}
  .food-list{list-style:none}
  .food-list li{display:flex;align-items:flex-start;font-size:8.5px;font-weight:500;line-height:1.15;margin-bottom:8px}
  .food-list li::before{content:"";flex:none;width:8px;height:8px;border-radius:50%;background:var(--dot,#c98a4a);margin:1px 6px 0 0}

  .tips-band{left:0;top:540px;width:690px;height:185px}
  .tips-title{left:0;top:570px;width:690px;text-align:center;font-family:"Archivo Black",sans-serif;font-size:20px;color:var(--black)}
  .tips{left:40px;top:605px;width:620px;display:flex;justify-content:space-between}
  .tip{width:98px;color:var(--black)}
  .tip-icon{width:28px;height:28px;border-radius:6px;background:linear-gradient(135deg,var(--orange),var(--blue));margin:0 0 8px 8px}
  .tip b{display:block;font-size:9px;font-weight:900;line-height:1.05}
  .tip small{display:block;font-size:7.5px;font-weight:500;color:#5a4a00;margin-top:3px;line-height:1.15}

  .habits{left:28px;top:748px;width:634px;height:122px;border:1.5px solid #5a5a5a;border-radius:12px}
  .habits-pill{left:275px;top:735px;width:140px;height:24px;border-radius:12px;background:var(--green);color:var(--ink);font-family:"Archivo Black",sans-serif;font-size:15px;letter-spacing:6px;display:flex;align-items:center;justify-content:center}
  .habit{position:absolute;top:765px;width:110px;height:110px}
  .habit svg{position:absolute;inset:0}
  .habit p{position:absolute;left:22px;top:32px;width:66px;height:46px;display:flex;align-items:center;justify-content:center;text-align:center;font-size:8.5px;font-weight:700;color:var(--black);line-height:1.1}
  .habits-label{left:270px;top:778px;width:150px;text-align:center;font-size:27px;line-height:1}
  .site{left:0;top:873px;width:690px;text-align:center;font-size:13px;font-weight:800;letter-spacing:4px;color:var(--yellow);background:var(--black)}
</style>
</head>
<body>

<!-- Page 1: Nutrition Blueprint -->
<section class="sheet sheet--blueprint">
  <div class="abs hero-photo" role="img" aria-label="Darkened gym photo with weight plates"></div>
  <div class="abs display title-week">6 Week</div>
  <div class="abs display title-season">Autumn</div>
  <div class="abs display title-forge">Forge</div>
  <div class="abs display title-sub">Nutrition<br>Blueprint</div>

  <div class="abs brand">
    <div class="brand-name">VoltaKor</div>
    <div class="brand-tag">PERSONAL GROUP TRAINING</div>
  </div>

  <div class="abs goal-label">GOAL</div>
  <div class="abs goal-head">DROP BODY FAT,<br>MAINTAIN LEAN<br>MUSCLE, AND<br>BOOST ENERGY</div>
  <div class="abs goal-body">without giving up real food or living in the kitchen.</div>

  <div class="abs eliminate">
    <h2 class="display elim-title">Foods &amp; Drinks<br><span class="orange">To Eliminate</span></h2>
    <p class="elim-note">(OR GREATLY REDUCE)</p>
    <p class="elim-desc">These are the biggest culprits sabotaging fat loss -highly palatable, calorie-dense, and metabolically disruptive:</p>
    <ul class="elim-list">
      <li><div class="elim-icon"><span role="img" aria-label="Soda icon"></span></div><div class="elim-item"><b>SUGARY DRINKS</b><small>Sodas, energy drinks, sweet teas, juice blends</small></div></li>
      <li><div class="elim-icon"><span role="img" aria-label="Coffee cup icon"></span></div><div class="elim-item"><b>FANCY COFFEE DRINKS</b><small>Frostinos, sugary creamers, flavor pumps</small></div></li>
      <li><div class="elim-icon"><span role="img" aria-label="Fast food icon"></span></div><div class="elim-item"><b>FAST FOOD &amp; FRIED FOODS</b><small>Even “grilled” items often packed with oils</small></div></li>
      <li><div class="elim-icon"><span role="img" aria-label="Chips bag icon"></span></div><div class="elim-item"><b>PACKAGED SNACKS</b><small>Chips, cookies, granola bars, trail mix with candy</small></div></li>
      <li><div class="elim-icon"><span role="img" aria-label="Cupcake icon"></span></div><div class="elim-item"><b>BAKED GOODS</b><small>Donuts, muffins, pastries, bagels with cream cheese</small></div></li>
      <li><div class="elim-icon"><span role="img" aria-label="Drinks icon"></span></div><div class="elim-item"><b>ALCOHOL</b><small>Especially beer and sugary mixers</small></div></li>
      <li><div class="elim-icon"><span role="img" aria-label="Bread icon"></span></div><div class="elim-item"><b>PROCESSED CARBS</b><small>White breads, crackers, pasta</small></div></li>
      <li><div class="elim-icon"><span role="img" aria-label="Cheese icon"></span></div><div class="elim-item"><b>CHEESE-HEAVY MEALS</b><small>Pizza, nachos, quesadillas</small></div></li>
      <li><div class="elim-icon"><span role="img" aria-label="Sausage icon"></span></div><div class="elim-item"><b>HIGH-FAT DELI MEATS</b><small>Salami, pepperoni, sausage</small></div></li>
      <li><div class="elim-icon"><span role="img" aria-label="Condiment bottles icon"></span></div><div class="elim-item"><b>SAUCES &amp; CONDIMENTS<br>LOADED WITH SUGAR</b><small>Ketchup, BBQ sauce, honey mustard</small></div></li>
    </ul>
  </div>

  <h2 class="abs display swaps-title">Smart Swaps<br><span class="yellow">For Fat Loss</span></h2>
  <p class="abs swaps-desc">Instead of cutting everything and feeling deprived, make these easy grocery-store swaps that still satisfy cravings without killing your progress:</p>
  <div class="pill pill--craving">CRAVING</div>
  <div class="pill pill--instead">TRY THIS INSTEAD</div>

  <table class="abs swap-table">
    <tbody>
      <tr><td class="swap-craving">SODA</td><td class="swap-arrow"><svg width="30" height="24" viewBox="0 0 30 24"><path d="M4 10a11 8 0 0 1 20-3" fill="none" stroke="#3fae49" stroke-width="3.5"/><path d="M26 14a11 8 0 0 1-20 3" fill="none" stroke="#3fae49" stroke-width="3.5"/><path d="M20 2l7 4-7 4z" fill="#3fae49"/><path d="M10 22l-7-4 7-4z" fill="#3fae49"/></svg></td><td class="swap-text">Sparkling water with lime, Zestiva, or plain water with fruit infusions Fancy Coffee</td></tr>
      <tr><td class="swap-craving">FANCY<br>COFFEE</td><td class="swap-arrow"><svg width="30" height="24" viewBox="0 0 30 24"><path d="M4 10a11 8 0 0 1 20-3" fill="none" stroke="#3fae49" stroke-width="3.5"/><path d="M26 14a11 8 0 0 1-20 3" fill="none" stroke="#3fae49" stroke-width="3.5"/><path d="M20 2l7 4-7 4z" fill="#3fae49"/><path d="M10 22l-7-4 7-4z" fill="#3fae49"/></svg></td><td class="swap-text">Coffee with unsweetened almond milk + stevia drops or cinnamon</td></tr>
      <tr><td class="swap-craving">CHIPS</td><td class="swap-arrow"><svg width="30" height="24" viewBox="0 0 30 24"><path d="M4 10a11 8 0 0 1 20-3" fill="none" stroke="#3fae49" stroke-width="3.5"/><path d="M26 14a11 8 0 0 1-20 3" fill="none" stroke="#3fae49" stroke-width="3.5"/><path d="M20 2l7 4-7 4z" fill="#3fae49"/><path d="M10 22l-7-4 7-4z" fill="#3fae49"/></svg></td><td class="swap-text">Rice cakes, roasted chickpeas, or crunchy cucumber with Tangrella</td></tr>
      <tr><td class="swap-craving">ICE CREAM</td><td class="swap-arrow"><svg width="30" height="24" viewBox="0 0 30 24"><path d="M4 10a11 8 0 0 1 20-3" fill="none" stroke="#3fae49" stroke-width="3.5"/><path d="M26 14a11 8 0 0 1-20 3" fill="none" stroke="#3fae49" stroke-width="3.5"/><path d="M20 2l7 4-7 4z" fill="#3fae49"/><path d="M10 22l-7-4 7-4z" fill="#3fae49"/></svg></td><td class="swap-text">Frozen banana blended with protein powder (DIY “nice cream”)</td></tr>
      <tr><td class="swap-craving">CANDY</td><td class="swap-arrow"><svg width="30" height="24" viewBox="0 0 30 24"><path d="M4 10a11 8 0 0 1 20-3" fill="none" stroke="#3fae49" stroke-width="3.5"/><path d="M26 14a11 8 0 0 1-20 3" fill="none" stroke="#3fae49" stroke-width="3.5"/><path d="M20 2l7 4-7 4z" fill="#3fae49"/><path d="M10 22l-7-4 7-4z" fill="#3fae49"/></svg></td><td class="swap-text">Berries, apples or dark chocolate squares (85%+)</td></tr>
      <tr><td class="swap-craving">PASTA</td><td class="swap-arrow"><svg width="30" height="24" viewBox="0 0 30 24"><path d="M4 10a11 8 0 0 1 20-3" fill="none" stroke="#3fae49" stroke-width="3.5"/><path d="M26 14a11 8 0 0 1-20 3" fill="none" stroke="#3fae49" stroke-width="3.5"/><path d="M20 2l7 4-7 4z" fill="#3fae49"/><path d="M10 22l-7-4 7-4z" fill="#3fae49"/></svg></td><td class="swap-text">Zucchini noodles, chickpea pasta, or cauliflower rice</td></tr>
      <tr><td class="swap-craving">PIZZA</td><td class="swap-arrow"><svg width="30" height="24" viewBox="0 0 30 24"><path d="M4 10a11 8 0 0 1 20-3" fill="none" stroke="#3fae49" stroke-width="3.5"/><path d="M26 14a11 8 0 0 1-20 3" fill="none" stroke="#3fae49" stroke-width="3.5"/><path d="M20 2l7 4-7 4z" fill="#3fae49"/><path d="M10 22l-7-4 7-4z" fill="#3fae49"/></svg></td><td class="swap-text">Egg white wraps or low-carb tortillas with turkey pepperoni and light cheese</td></tr>
      <tr><td class="swap-craving">ALCOHOL</td><td class="swap-arrow"><svg width="30" height="24" viewBox="0 0 30 24"><path d="M4 10a11 8 0 0 1 20-3" fill="none" stroke="#3fae49" stroke-width="3.5"/><path d="M26 14a11 8 0 0 1-20 3" fill="none" stroke="#3fae49" stroke-width="3.5"/><path d="M20 2l7 4-7 4z" fill="#3fae49"/><path d="M10 22l-7-4 7-4z" fill="#3fae49"/></svg></td><td class="swap-text">Limit to 1x/week if needed</td></tr>
      <tr><td class="swap-craving">SANDWICH<br>BREAD</td><td class="swap-arrow"><svg width="30" height="24" viewBox="0 0 30 24"><path d="M4 10a11 8 0 0 1 20-3" fill="none" stroke="#3fae49" stroke-width="3.5"/><path d="M26 14a11 8 0 0 1-20 3" fill="none" stroke="#3fae49" stroke-width="3.5"/><path d="M20 2l7 4-7 4z" fill="#3fae49"/><path d="M10 22l-7-4 7-4z" fill="#3fae49"/></svg></td><td class="swap-text">Ezren bread, low-carb wraps, or lettuce wraps</td></tr>
      <tr><td class="swap-craving">HEAVY<br>SAUCES</td><td class="swap-arrow"><svg width="30" height="24" viewBox="0 0 30 24"><path d="M4 10a11 8 0 0 1 20-3" fill="none" stroke="#3fae49" stroke-width="3.5"/><path d="M26 14a11 8 0 0 1-20 3" fill="none" stroke="#3fae49" stroke-width="3.5"/><path d="M20 2l7 4-7 4z" fill="#3fae49"/><path d="M10 22l-7-4 7-4z" fill="#3fae49"/></svg></td><td class="swap-text">Mustard, salsa, hot sauce, coconut aminos, Greek yogurt-based dips</td></tr>
    </tbody>
  </table>
</section>

<!-- Page 2: Meal Plan Guide -->
<section class="sheet sheet--guide">
  <div class="abs display guide-kicker">Build-Your-Own</div>
  <h1 class="abs display guide-title">Meal Plan Guide</h1>
  <p class="abs guide-intro">USE THESE FIT-FRIENDLY FOOD LISTS TO MIX &amp; MATCH MEALS.<br>YOUR JOB: <span style="font-weight:500">choose</span> <span class="c-blue">1 protein</span>, <span class="c-yellow" style="color:var(--yellow)">1 carb (if desired)</span>, <span style="font-weight:500">and</span> <span class="c-orange">1 fat</span> <span style="font-weight:500">or</span> <span class="c-green">veggie</span> <span style="font-weight:500">at each meal.</span><br>KEEP IT SIMPLE, KEEP IT CONSISTENT.</p>

  <div class="abs food-col" style="left:28px;--dot:#c77a5a">
    <div class="col-pill col-pill--proteins">PROTEINS</div>
    <p class="col-note">Choose 1<br>per meal/snack</p>
    <ul class="food-list">
      <li>Chicken breast or thighs (air fried or grilled)</li>
      <li>Lean ground beef (90/10 or better)</li>
      <li>Ground turkey or turkey breast</li>
      <li>Center-cut pork chops</li>
      <li>Eggs / Egg whites</li>
      <li>Tuna (canned in water)</li>
      <li>Salmon or white fish</li>
      <li>Shrimp</li>
      <li>Greek yogurt (plain, low sugar)</li>
      <li>Cottage cheese (low-fat)</li>
      <li>Protein powder (whey or plant-based)</li>
      <li>Deli turkey (low-sodium)</li>
    </ul>
  </div>
  <div class="abs food-col" style="left:190px;--dot:#e0a23a">
    <div class="col-pill col-pill--carbs">CARBS</div>
    <p class="col-note">choose 1–2 servings per day, timed post-workout or morning</p>
    <ul class="food-list">
      <li>Jasmine or basmati rice (white or brown)</li>
      <li>Sweet potatoes or yams</li>
      <li>Rolled oats or steel cut oats</li>
      <li>Quinoa</li>
      <li>Ezren bread</li>
      <li>Rice cakes</li>
      <li>Berries (blueberries, raspberries, strawberries)</li>
      <li>Apples / Bananas</li>
      <li>Chickpeas or black beans (in moderation)</li>
    </ul>
  </div>
  <div class="abs food-col" style="left:352px;--dot:#8bb040">
    <div class="col-pill col-pill--fats">FATS</div>
    <p class="col-note">Add small amounts to meals, 2–4 servings/day</p>
    <ul class="food-list">
      <li>Avocado or guacamole</li>
      <li>Olive oil or avocado oil (cooking or drizzle)</li>
      <li>Nut butters (almond, peanut – natural only)</li>
      <li>Whole eggs</li>
      <li>Nuts (almonds, walnuts – portion controlled)</li>
      <li>Chia seeds or flax seeds</li>
    </ul>
  </div>
  <div class="abs food-col" style="left:512px;--dot:#4fae3a">
    <div class="col-pill col-pill--veggies">VEGGIES</div>
    <p class="col-note">Unlimited<br>fill your plate!</p>
    <ul class="food-list">
      <li>Spinach, kale, arugula</li>
      <li>Zucchini, asparagus, bell peppers</li>
      <li>Broccoli, cauliflower, green beans</li>
      <li>Cucumber, tomatoes, shredded carrots</li>
      <li>Mixed greens or salad kits (watch the dressing)</li>
    </ul>
  </div>

  <svg class="abs tips-band" viewBox="0 0 690 185" preserveAspectRatio="none" aria-hidden="true">
    <polygon fill="#f9d00f" points="0,12 20,4 38,14 60,2 84,10 110,0 130,12 158,5 180,14 204,3 232,11 256,2 280,13 306,4 330,12 356,1 380,10 404,3 430,13 456,5 478,12 504,2 530,11 552,4 578,13 602,3 628,10 652,2 672,12 690,5 690,172 668,182 644,170 620,184 594,174 570,182 546,171 520,183 496,173 470,181 446,170 420,184 396,174 370,182 346,171 320,183 296,172 270,182 246,170 220,184 196,174 170,182 146,171 120,183 96,172 70,182 46,170 22,184 0,174"/>
  </svg>
  <div class="abs tips-title">★ ★ ★ &nbsp;BONUS TIPS FOR MAXIMUM RESULTS&nbsp; ★ ★ ★</div>
  <div class="abs tips">
    <div class="tip"><div class="tip-icon" role="img" aria-label="Water bottles icon"></div><b>DRINK<br>80-120 OZ.<br>WATER DAILY</b><small>hydration is key for fat loss and muscle performance</small></div>
    <div class="tip"><div class="tip-icon" role="img" aria-label="Meal plate icon"></div><b>EAT<br>3-4 MEALS<br>PER DAY</b><small>spaced every 3–4 hours</small></div>
    <div class="tip"><div class="tip-icon" role="img" aria-label="Protein strand icon"></div><b>INCLUDE<br>PROTEIN IN<br>EVERY MEAL</b><small>to stabilize blood sugar and support muscle</small></div>
    <div class="tip"><div class="tip-icon" role="img" aria-label="Meal container icon"></div><b>POST<br>WORKOUT MEAL<br>= PROTEIN+ CARB,</b><small>no added fats</small></div>
    <div class="tip"><div class="tip-icon" role="img" aria-label="Protein shake icon"></div><b>UP TO, TWO<br>PROTEIN SHAKES<br>PER DAY IS ALLOWED</b><small>especially post-workout or on busy days</small></div>
    <div class="tip"><div class="tip-icon" role="img" aria-label="Treat plate icon"></div><b>LIMIT<br>“TREAT” MEALS<br>TO 1 PER WEEK</b><small>(keep it controlled)</small></div>
  </div>

  <div class="abs habits"></div>
  <div class="abs habits-pill">OPTIONAL</div>

  <div class="habit" style="left:38px">
    <svg viewBox="0 0 110 110"><circle cx="55" cy="55" r="46" fill="#fff"/><circle cx="55" cy="55" r="46" fill="none" stroke="#f7941d" stroke-width="9" stroke-dasharray="96 193" transform="rotate(150 55 55)"/><circle cx="55" cy="55" r="46" fill="none" stroke="#3a4fb8" stroke-width="9" stroke-dasharray="96 193" transform="rotate(270 55 55)"/><circle cx="55" cy="55" r="46" fill="none" stroke="#3fae49" stroke-width="9" stroke-dasharray="96 193" transform="rotate(30 55 55)"/></svg>
    <p>Weigh in once per week (same day/time)</p>
  </div>
  <div class="habit" style="left:158px">
    <svg viewBox="0 0 110 110"><circle cx="55" cy="55" r="46" fill="#fff"/><circle cx="55" cy="55" r="46" fill="none" stroke="#f7941d" stroke-width="9" stroke-dasharray="96 193" transform="rotate(150 55 55)"/><circle cx="55" cy="55" r="46" fill="none" stroke="#3a4fb8" stroke-width="9" stroke-dasharray="96 193" transform="rotate(270 55 55)"/><circle cx="55" cy="55" r="46" fill="none" stroke="#3fae49" stroke-width="9" stroke-dasharray="96 193" transform="rotate(30 55 55)"/></svg>
    <p>Prep 2–3 proteins and veggies on Sunday</p>
  </div>
  <div class="abs display habits-label">Habits<br>To<br>Stack</div>
  <div class="habit" style="left:410px">
    <svg viewBox="0 0 110 110"><circle cx="55" cy="55" r="46" fill="#fff"/><circle cx="55" cy="55" r="46" fill="none" stroke="#f7941d" stroke-width="9" stroke-dasharray="96 193" transform="rotate(150 55 55)"/><circle cx="55" cy="55" r="46" fill="none" stroke="#3a4fb8" stroke-width="9" stroke-dasharray="96 193" transform="rotate(270 55 55)"/><circle cx="55" cy="55" r="46" fill="none" stroke="#3fae49" stroke-width="9" stroke-dasharray="96 193" transform="rotate(30 55 55)"/></svg>
    <p>Keep a visible “YES/NO” food list on the fridge</p>
  </div>
  <div class="habit" style="left:534px">
    <svg viewBox="0 0 110 110"><circle cx="55" cy="55" r="46" fill="#fff"/><circle cx="55" cy="55" r="46" fill="none" stroke="#f7941d" stroke-width="9" stroke-dasharray="96 193" transform="rotate(150 55 55)"/><circle cx="55" cy="55" r="46" fill="none" stroke="#3a4fb8" stroke-width="9" stroke-dasharray="96 193" transform="rotate(270 55 55)"/><circle cx="55" cy="55" r="46" fill="none" stroke="#3fae49" stroke-width="9" stroke-dasharray="96 193" transform="rotate(30 55 55)"/></svg>
    <p>Add a short 10-min walk after dinner to boost digestion</p>
  </div>

  <div class="abs site">JOINVOLTAKOR.COM</div>
</section>

</body>
</html>
```